Veltarum

Standard Business Card design.
Sample two-sided design uploaded. White front, Black back.
Would like white shield to be on all black background side.
Willing to look at a couple creative designs, but nothing crazy.
Preference for a classic, confident, strong design.

```html
<!DOCTYPE html>
<html lang="en">
<head>
<meta charset="utf-8">
<title>Veltarum Business Card</title>
<link href="https://fonts.googleapis.com/css2?family=Montserrat:wght@400;500;700&display=swap" rel="stylesheet">
<style>
  :root {
    --backdrop: #4a4a4a;
    --card-black: #1a1a1a;
    --ink-white: #ffffff;
    --ink-soft: #e6e6e6;
    --emboss: #262626;
  }
  * { margin: 0; padding: 0; box-sizing: border-box; }
  html, body { width: 1200px; height: 780px; overflow: hidden; }
  body {
    background: var(--backdrop);
    font-family: "Montserrat", sans-serif;
    color: var(--ink-white);
    position: relative;
  }
  .card {
    position: absolute;
    width: 540px;
    height: 308px;
    background: var(--card-black);
    border-radius: 22px;
    box-shadow: 0 18px 40px rgba(0,0,0,0.35);
    overflow: hidden;
  }
  .card--front { left: 40px; top: 236px; }
  .card--back { left: 620px; top: 236px; }

  .brand {
    display: flex;
    align-items: center;
    gap: 16px;
    position: absolute;
  }
  .brand__mark {
    background: var(--ink-white);
    flex: none;
  }
  .brand__name {
    font-weight: 500;
    letter-spacing: 0.12em;
    color: var(--ink-white);
    line-height: 1;
  }
  .card--front .brand {
    left: 50%; top: 50%;
    transform: translate(-50%, -50%);
    gap: 22px;
  }
  .card--front .brand__mark { width: 44px; height: 44px; }
  .card--front .brand__name { font-size: 48px; }

  .card--back .brand { left: 34px; top: 38px; gap: 12px; }
  .card--back .brand__mark { width: 24px; height: 24px; }
  .card--back .brand__name { font-size: 26px; }

  .holder {
    position: absolute;
    right: 34px;
    top: 36px;
    text-align: right;
  }
  .holder__name {
    font-weight: 700;
    font-size: 18px;
    letter-spacing: 0.03em;
    text-transform: uppercase;
  }
  .holder__title {
    font-size: 13px;
    margin-top: 4px;
    color: var(--ink-soft);
  }

  .watermark {
    position: absolute;
    right: -8px;
    top: 118px;
    font-weight: 700;
    font-size: 86px;
    letter-spacing: 0.02em;
    color: var(--emboss);
    line-height: 1;
    white-space: nowrap;
  }

  .contact {
    position: absolute;
    left: 34px;
    bottom: 28px;
    font-size: 13px;
    color: var(--ink-soft);
    line-height: 1.45;
  }
  .contact__address { margin-bottom: 16px; }
  .contact__list { list-style: none; }
  .contact__item { display: flex; align-items: center; gap: 10px; }
  .contact__icon { width: 12px; height: 12px; fill: var(--ink-soft); flex: none; }
</style>
</head>
<body>

  <section class="card card--front" aria-label="Card front">
    <div class="brand">
      <span class="brand__mark"></span>
      <span class="brand__name">VELTARUM</span>
    </div>
  </section>

  <section class="card card--back" aria-label="Card back">
    <div class="watermark" aria-hidden="true">VELTARUM</div>

    <div class="brand">
      <span class="brand__mark"></span>
      <span class="brand__name">VELTARUM</span>
    </div>

    <div class="holder">
      <p class="holder__name">Daniel Marsh</p>
      <p class="holder__title">Managing Director</p>
    </div>

    <div class="contact">
      <p class="contact__address">Your address, City<br>State, Zip 1234</p>
      <ul class="contact__list">
        <li class="contact__item">
          <svg class="contact__icon" viewBox="0 0 12 12"><path d="M2.5 0.8l2 2.2-1 1.3c.7 1.5 1.8 2.6 3.3 3.3l1.3-1 2.2 2-1.2 1.9C5 10.3 1.7 7 0.8 2z"/></svg>
          <span>123 456 789</span>
        </li>
        <li class="contact__item">
          <svg class="contact__icon" viewBox="0 0 12 12"><path d="M0.5 2.5h11v7h-11z M1 3l5 3.5L11 3" stroke="#1a1a1a" stroke-width="0.8"/></svg>
          <span>info@yourmail.com</span>
        </li>
        <li class="contact__item">
          <svg class="contact__icon" viewBox="0 0 12 12"><circle cx="6" cy="6" r="5.5"/><path d="M0.5 6h11M6 0.5c-2.5 3-2.5 8 0 11M6 0.5c2.5 3 2.5 8 0 11" stroke="#1a1a1a" stroke-width="0.7" fill="none"/></svg>
          <span>www.yourwebsite.com</span>
        </li>
      </ul>
    </div>
  </section>

</body>
</html>
```